Letterhead to Introduce a 'Sister' Company.

What I am needing is a design for a letter head to introduce our current customers base of (KT Alarm) customers to our new service, 'Kestrel Tide Solar Brokers'

```html
<!DOCTYPE html>
<html lang="en">
<head>
<meta charset="utf-8">
<title>Kestrel Tide Solar Brokers – Letterhead</title>
<link rel="stylesheet" href="https://fonts.googleapis.com/css2?family=Roboto:wght@400;500;700&display=swap">
<style>
  :root {
    --backdrop: #e2e3e4;
    --paper: #f4f4f4;
    --sun-orange: #ef981f;
    --sun-light: #f7c677;
    --navy: #10447a;
    --ink: #1d1d1f;
    --faint-mark: #e9ecef;
    --white: #ffffff;
  }
  * { margin: 0; padding: 0; box-sizing: border-box; }
  html, body {
    width: 1200px; height: 1200px; overflow: hidden;
    background: var(--backdrop);
    font-family: "Roboto", Arial, sans-serif;
  }
  .canvas { position: relative; width: 1200px; height: 1200px; }
  .letterhead {
    position: absolute; left: 152px; top: 21px;
    width: 918px; height: 1186px;
    background: var(--paper);
    transform: scale(0.976); transform-origin: top left;
    overflow: hidden;
  }
  .bands { position: absolute; inset: 0; width: 918px; height: 1186px; }
  .brand {
    position: absolute; top: 112px; right: 66px; width: 260px;
    text-align: center; color: var(--navy);
  }
  .brand-dot {
    display: block; width: 44px; height: 44px; border-radius: 50%;
    background: var(--sun-orange); margin: 0 auto 14px;
  }
  .brand-name {
    font-weight: 500; font-size: 27px; letter-spacing: 0.5px; line-height: 1.05;
  }
  .brand-sub {
    font-weight: 500; font-size: 13px; letter-spacing: 2px; margin-top: 4px;
  }
  .faint-mark {
    position: absolute; left: 0; right: 0; top: 530px;
    text-align: center; color: var(--faint-mark);
    font-weight: 700; font-size: 96px; line-height: 1.05;
  }
  .contact {
    position: absolute; left: 64px; top: 1064px;
    font-size: 14px; color: var(--ink); line-height: 18px;
  }
  .contact-address { margin-bottom: 5px; }
  .contact-line { display: flex; align-items: center; gap: 4px; }
  .contact-line svg { width: 12px; height: 12px; flex: none; }
  .parent-credit {
    position: absolute; right: 60px; top: 1116px;
    color: var(--white); font-size: 17px; font-weight: 500;
  }
  .parent-credit .parent-name { font-size: 22px; margin-left: 4px; }
</style>
</head>
<body>
<main class="canvas">
  <article class="letterhead">
    <svg class="bands" viewBox="0 0 918 1186" aria-hidden="false">
      <defs>
        <radialGradient id="sunGlow" cx="0.35" cy="0.9" r="0.8">
          <stop offset="0" stop-color="var(--sun-light)"/>
          <stop offset="1" stop-color="var(--sun-orange)"/>
        </radialGradient>
      </defs>
      <polygon class="top-band" points="0,0 918,0 0,143" fill="var(--sun-orange)"/>
      <polygon class="sun-art" role="img" aria-label="Rising sun with radiating rays" points="0,0 268,0 268,101 0,143" fill="url(#sunGlow)"/>
      <polygon class="bottom-band" points="918,1043 918,1186 0,1186" fill="var(--navy)"/>
    </svg>

    <header class="brand">
      <span class="brand-dot"></span>
      <div class="brand-name">KESTREL TIDE</div>
      <div class="brand-sub">SOLAR BROKERS</div>
    </header>

    <div class="faint-mark">Kestrel<br>Tide</div>

    <footer class="contact">
      <p class="contact-address">PO Box 2270, Harborview, WA 98012</p>
      <p class="contact-line">
        <svg viewBox="0 0 12 12"><path d="M2.5 1 L4.5 1 L5.3 3.4 L4 4.4 Q5 6.8 7.6 8 L8.6 6.7 L11 7.5 L11 9.5 Q10.5 11 8.8 11 Q1 10 1 2.8 Q1 1 2.5 1Z" fill="var(--navy)"/></svg>
        888-555-0192
      </p>
      <p class="contact-line">
        <svg viewBox="0 0 12 12"><rect x="1" y="2.5" width="10" height="7" fill="none" stroke="var(--navy)" stroke-width="1.2"/><path d="M1 2.5 L6 6.5 L11 2.5" fill="none" stroke="var(--navy)" stroke-width="1.2"/></svg>
        info@kthomesecure.example
      </p>
      <p class="contact-line">
        <svg viewBox="0 0 12 12"><circle cx="6" cy="6" r="4.8" fill="none" stroke="var(--navy)" stroke-width="1"/><ellipse cx="6" cy="6" rx="2" ry="4.8" fill="none" stroke="var(--navy)" stroke-width="1"/><path d="M1.2 6 H10.8" stroke="var(--navy)" stroke-width="1"/></svg>
        www.kthomesecure.example
      </p>
    </footer>

    <div class="parent-credit">by <span class="parent-name">KT Alarm</span></div>
  </article>
</main>
</body>
</html>
```